Modify mobile web Photoshop design to make them look great

We need to choose and refine the stock image to look great on 5 mobile web pages: 1) Hourglass image on home screen, 2) Sofa image on registration screen, 3) Loveseat image on login screen, 4) Lamp for reminder screen, and 5) Bed for ratings / score screen. Sample photos denote what customer wants, but they are just downloaded from Vantry, and is not purchased stock photos. Designers need to show that the updated photos used are properly purchased from stock photo source. Photoshop files for all 5 mobile web pages are provided. Artists are requested to edit and submit the 5 photoshop files and make them look as good as possible with the constraints above. No change is needed on the layout or anything beside the 5 stock images, but subtle refinements are OK if you believe it would improve the overall design without affecting the art direction.

Target Market(s)

Travel, Lifestyle

Industry/Entity Type

Hospitality

Font styles to use
Sans Serif

Requirements
Must have
• Stock photos must be properly licensed, artists must put updated stock photos back into supplied photoshop source files, updated look and feel should have the same general art direction, images must be hourglass, sofa, loveseat, lamp and bed
Nice to have
• Minor and very subtle touchup of other elements without affecting any design work of the layout such as color scheme
Should not have
• Should not affect art direction, identity and color of all design and layout elements, should not use stock image other than the types specified (hourglass, sofa, loveseat, lamp and bed), should not use images not licensed from stock photo sites

```html
<!DOCTYPE html>
<html lang="en">
<head>
<meta charset="utf-8">
<title>nestly.co – Register</title>
<link rel="stylesheet" href="https://fonts.googleapis.com/css2?family=Source+Sans+3:wght@400;600;800&display=swap">
<style>
  :root {
    --ink: #111111;
    --field-text: #5a5a5a;
    --field-bg: #ffffff;
    --divider: #b9b9b9;
    --purple: #b07fd8;
    --teal: #0e9593;
    --magenta: #a4127c;
    --peach: #f2b384;
    --slate: #4c5a63;
    --page: #e8e4e0;
    --card: rgba(246, 244, 242, 0.72);
  }
  * { box-sizing: border-box; margin: 0; padding: 0; }
  html, body { width: 676px; height: 1200px; overflow: hidden; }
  body {
    position: relative;
    background: var(--page);
    font-family: "Source Sans 3", sans-serif;
  }
  .hero-photo {
    position: absolute; left: 0; top: 0; width: 676px; height: 800px;
    background:
      linear-gradient(180deg, rgba(232,228,224,0) 80%, var(--page) 100%),
      linear-gradient(180deg, #dcd5d0 0%, #e5e0dc 45%, #d9d6d2 62%, #cfcdca 85%, #e2dfdb 100%);
  }
  .top-bar { position: absolute; left: 0; top: 0; width: 676px; height: 96px; }
  .back-button { position: absolute; left: 36px; top: 28px; }
  .brand {
    position: absolute; left: 0; right: 0; top: 14px; text-align: center;
    font-weight: 800; font-size: 52px; letter-spacing: -2px; color: var(--ink); line-height: 1;
  }
  .menu-button { position: absolute; left: 601px; top: 38px; }
  .register-card {
    position: absolute; left: 26px; top: 343px; width: 622px; height: 560px;
    background: var(--card); border: 1px solid rgba(255,255,255,0.9); border-radius: 10px;
  }
  .field {
    position: absolute; left: 55px; width: 508px; height: 49px;
    background: var(--field-bg); border-bottom: 1px solid var(--line);
    display: flex; align-items: center;
  }
  .field-icon {
    width: 56px; height: 100%; display: flex; align-items: center; justify-content: center;
    border-right: 1px solid var(--divider); margin: 8px 0; height: 33px;
  }
  .field-label { font-size: 18px; color: var(--field-text); padding-left: 12px; flex: 1; }
  .dob-tag { font-size: 15px; color: var(--magenta); font-weight: 600; }
  .calendar { margin-right: 14px; }
  .register-button {
    position: absolute; left: 56px; top: 476px; width: 506px; height: 47px;
    background: var(--peach); border: none; border-radius: 4px;
    color: #fff; font-family: "Source Sans 3", sans-serif; font-size: 22px; font-weight: 400;
  }
  .pager { position: absolute; left: 267px; top: 1091px; display: flex; gap: 13px; }
  .pager span { width: 20px; height: 20px; border-radius: 50%; }
</style>
</head>
<body>
  <div class="hero-photo" role="img" aria-label="Light living room with a grey fabric sofa, patterned cushions and a small white side table"></div>

  <header class="top-bar">
    <svg class="back-button" width="26" height="36" viewBox="0 0 26 36"><path d="M21 3 L6 18 L21 33" fill="none" stroke="#111" stroke-width="4"/></svg>
    <div class="brand">nestly.co</div>
    <svg class="menu-button" width="36" height="18" viewBox="0 0 36 18"><path d="M0 1h35M0 9h35M0 17h35" stroke="#111" stroke-width="2"/></svg>
  </header>

  <form class="register-card">
    <div class="field" style="top:46px; --line: var(--purple);">
      <span class="field-icon"><svg width="24" height="28" viewBox="0 0 24 28"><circle cx="12" cy="8" r="6" fill="none" stroke="#b07fd8" stroke-width="1.5"/><path d="M2 27c0-7 4-11 10-11s10 4 10 11z" fill="none" stroke="#b07fd8" stroke-width="1.5"/></svg></span>
      <span class="field-label">Full Name</span>
    </div>
    <div class="field" style="top:117px; --line: var(--slate);">
      <span class="field-icon"><svg width="32" height="22" viewBox="0 0 32 22"><rect x="1" y="1" width="30" height="20" rx="2" fill="none" stroke="#0e9593" stroke-width="1.6"/><circle cx="10" cy="8" r="3" fill="none" stroke="#0e9593" stroke-width="1.4"/><path d="M5 17c0-4 2-5 5-5s5 1 5 5z" fill="none" stroke="#0e9593" stroke-width="1.4"/><path d="M19 8h8M19 12h8" stroke="#0e9593" stroke-width="1.6"/></svg></span>
      <span class="field-label" style="padding-left:16px">ID Number</span>
    </div>
    <div class="field" style="top:188px; --line: var(--magenta);">
      <span class="field-icon"><span class="dob-tag">DOB</span></span>
      <span class="field-label" style="padding-left:16px">06/09/1980</span>
      <svg class="calendar" width="28" height="28" viewBox="0 0 28 28"><rect x="2" y="4" width="24" height="22" rx="2" fill="none" stroke="#a4127c" stroke-width="2.4"/><rect x="2" y="4" width="24" height="6" fill="#a4127c"/><path d="M8 1v6M20 1v6" stroke="#a4127c" stroke-width="2.4"/><g fill="#a4127c"><rect x="6" y="13" width="4" height="3"/><rect x="12" y="13" width="4" height="3"/><rect x="18" y="13" width="4" height="3"/><rect x="6" y="19" width="4" height="3"/><rect x="12" y="19" width="4" height="3"/><rect x="18" y="19" width="4" height="3"/></g></svg>
    </div>
    <div class="field" style="top:258px; --line: var(--peach);">
      <span class="field-icon"><svg width="18" height="30" viewBox="0 0 18 30"><rect x="1" y="1" width="16" height="28" rx="2" fill="#f2b384" stroke="#e89a60" stroke-width="1.2"/><rect x="3" y="5" width="12" height="19" fill="#f8c89f"/><circle cx="9" cy="26.5" r="1.2" fill="#fff"/></svg></span>
      <span class="field-label">Mobile Number</span>
    </div>
    <div class="field" style="top:329px; --line: var(--slate);">
      <span class="field-icon"><svg width="26" height="26" viewBox="0 0 26 26"><circle cx="18" cy="8" r="6" fill="#0e9593"/><circle cx="19" cy="7" r="1.8" fill="#fff"/><path d="M14 12 L3 23 L5 25 L7 23 L9 25 L11 23 L9 21 L16 14z" fill="#0e9593"/></svg></span>
      <span class="field-label">Set Password</span>
    </div>
    <div class="field" style="top:400px; --line: var(--purple);">
      <span class="field-icon"><svg width="24" height="16" viewBox="0 0 24 16"><rect x="0" y="0" width="24" height="16" fill="#b07fd8"/><path d="M0 0 L12 9 L24 0" fill="none" stroke="#fff" stroke-width="1.4"/></svg></span>
      <span class="field-label">Email</span>
    </div>
    <button class="register-button" type="button">REGISTER NOW</button>
  </form>

  <nav class="pager" aria-label="Screens">
    <span style="background:var(--purple)"></span>
    <span style="background:var(--teal)"></span>
    <span style="background:var(--magenta)"></span>
    <span style="background:var(--peach)"></span>
    <span style="background:var(--teal)"></span>
  </nav>
</body>
</html>
```